Riverbend Trusted Home Care-Flyer for Patients

Our Home Health Care Agency, Riverbend Trusted Home Care, is seeking a flyer to advertise our services. We would like our flyer to convey professionalism, classiness and sophistication. We want our agency to come across as one that is well-established and recognized as being first-rate within the field.

We also want to appear original; we want to stand out.

Our theme colors, blue and green, from our logo should be incorporated into the flyer's design (refer below).

The top of the page should say (in a clear, bold font)-Seeking Care for your Loved One?

Our Logo, followed by our slogan, "Lean On Those Nearby", should be in the center. (This should make it appear as if our agency is the obvious solution to the consumer's quest in finding suitable care for their family member). This should be in a big font.
Below that, our agency's services should be listed in a very noticeable font...yet smaller than what's written above that.
The text should read:
Our Services Include:
*Experienced Certified Home Health Aides/ Live In Home Health Aides/Companions
*Nursing Services
*Alzheimer’s and Dementia Care
*Respite Care
*Postoperative Care
*Post Rehabilitation Care
*Running Errands
*Light Housekeeping
*Assistance with Bathing, Feeding and Grooming
*Meal Preparation
*Laundry and Linen Washing
*Mail and Bill Organization
*Medication Management
*Accompanying to Doctor’s Appointments
*And much more!
Below that, in a smaller, yet noticeable font:
As seasoned professionals, we know how to help our clients navigate and fulfill their various health care needs. Those nearby are here to help you get the attention that you merit.
Call Riverbend Trusted Home Care today to learn more about our first-rate services!
Below that, in a larger font, our phone number, website, our e-mail address.
*Out contact information will be provided to the project’s winner*.

*Pictures of Caregivers helping elderly patient should be included in the advertisement as well. *

We provided advertisements of other Home Health Care Agencies attached below to use as a reference. Once again, while we are aiming for a similar idea; however, our goal is to stand out as the community's premiere home health care agency, the one that they want to choose. We want to be original as well!

Size: Standard Computer Paper Size. 8.5” x 11”.

Feel free to utilize your creative, designer flair!
We look forward to seeing the results!
Good luck!

Industry/Entity Type

Home Health Care

Font styles to use
Sans Serif

Requirements
Must have
• Refer above.
Nice to have
• Refer to attachment below to see how other home health care agencies advertise. While we are aiming for a similar idea, we would like to incorporate our logo, slogan and colors to make this flyer more unique and stand out. We would like to appear original.

```html
<!DOCTYPE html>
<html lang="en">
<head>
<meta charset="utf-8">
<title>Riverbend Trusted Home Care – Flyer</title>
<link rel="stylesheet" href="https://fonts.googleapis.com/css2?family=Source+Sans+3:wght@400;600;700;800&display=swap">
<style>
  :root {
    --navy: #262f6b;
    --green: #8cc63f;
    --green-dark: #7ab32e;
    --white: #ffffff;
    --page-bg: #e9e9e9;
    --text-navy: #262f6b;
    --grey-fade: #eeeff1;
  }
  * { box-sizing: border-box; margin: 0; padding: 0; }
  html, body {
    width: 989px; height: 1200px; overflow: hidden;
    background: var(--page-bg);
    font-family: "Source Sans 3", "Helvetica Neue", Arial, sans-serif;
  }
  .flyer {
    position: absolute; left: 44px; top: 19px;
    width: 900px; height: 1162px;
    background: linear-gradient(180deg, var(--white) 55%, var(--grey-fade) 90%, var(--white) 100%);
    overflow: hidden;
    box-shadow: 0 2px 8px rgba(0,0,0,.18);
  }
  .hero-photo {
    position: absolute; left: 0; top: 160px; width: 900px; height: 500px;
    background: linear-gradient(120deg, #a9cbe6 0%, #d7e6ef 40%, #9dc27a 75%, #c9dea6 100%);
  }
  .waves { position: absolute; left: 0; top: 0; width: 900px; height: 1162px; }

  .brand {
    position: absolute; left: 40px; top: 70px;
    display: flex; align-items: center; gap: 12px;
  }
  .brand-dot {
    width: 38px; height: 38px; border-radius: 50%; background: var(--green);
    flex: none;
  }
  .brand-name {
    font-weight: 800; font-size: 25px; line-height: 1.05; color: var(--navy);
    text-transform: uppercase; width: 250px;
  }

  .headline-block { position: absolute; right: 28px; top: 30px; text-align: right; }
  .kicker {
    font-weight: 700; font-size: 21px; color: var(--green); text-transform: uppercase;
    letter-spacing: .2px;
  }
  .headline {
    font-weight: 800; font-size: 43px; line-height: 1.08; color: var(--navy);
    text-transform: uppercase; margin-top: 4px;
  }

  .services { position: absolute; left: 40px; top: 686px; width: 400px; }
  .services h2 {
    font-weight: 800; font-size: 30px; color: var(--navy); text-transform: uppercase;
    letter-spacing: .2px; margin-bottom: 6px;
  }
  .services ul { list-style: none; }
  .services li {
    position: relative; padding-left: 22px;
    font-size: 15.5px; line-height: 21px; color: var(--text-navy); font-weight: 600;
  }
  .services li::before {
    content: "›"; position: absolute; left: 0; top: 4px;
    width: 13px; height: 13px; border-radius: 50%; background: var(--green);
    color: var(--white); font-size: 13px; line-height: 11px; text-align: center; font-weight: 700;
  }

  .intro {
    position: absolute; left: 482px; top: 680px; width: 382px;
    font-size: 14.5px; line-height: 20px; color: var(--text-navy); text-align: justify;
  }

  .cta {
    position: absolute; left: 482px; top: 779px; width: 381px; height: 125px;
    background: var(--navy); border-radius: 16px;
    color: var(--white); text-align: center;
    font-weight: 700; font-size: 16.5px; line-height: 22px; text-transform: uppercase;
    padding-top: 20px;
  }
  .cta-phone {
    position: absolute; left: 523px; top: 877px; width: 286px; height: 44px;
    background: var(--green); border-radius: 22px;
    display: flex; align-items: center; justify-content: center; gap: 12px;
    color: var(--white); font-weight: 700; font-size: 26px; letter-spacing: .5px;
  }
  .cta-phone svg { width: 24px; height: 24px; }

  .gallery { position: absolute; left: 485px; top: 934px; width: 400px; height: 134px; }
  .gallery-photo {
    position: absolute; top: 0; width: 134px; height: 134px; border-radius: 50%;
    border: 4px solid var(--white); box-shadow: 0 2px 6px rgba(0,0,0,.25);
  }
  .gallery-photo.one { left: 0; background: linear-gradient(135deg, #cfd9e6, #6d86a8); }
  .gallery-photo.two { left: 130px; background: linear-gradient(135deg, #e6dcd2, #b77b78); }
  .gallery-photo.three { left: 260px; background: linear-gradient(135deg, #d9cfa6, #3a3a3a); }

  .footer-rule { position: absolute; left: 44px; top: 1090px; width: 812px; height: 4px; background: var(--green); }
  .footer {
    position: absolute; left: 0; top: 1102px; width: 900px; height: 60px;
    background: var(--navy); color: var(--white);
    display: flex; align-items: center; justify-content: space-between;
    padding: 0 44px 0 44px; font-size: 17px;
  }
  .contact { display: flex; align-items: center; gap: 10px; }
  .contact svg { width: 18px; height: 18px; }
</style>
</head>
<body>
<main class="flyer">
  <div class="hero-photo" role="img" aria-label="Photo of a caregiver in scrubs holding hands with a smiling elderly woman outdoors"></div>

  <svg class="waves" viewBox="0 0 900 1162" aria-hidden="true">
    <path d="M0,0 H900 V200 C720,175 500,205 300,238 C180,256 80,252 0,240 Z" fill="#ffffff"/>
    <path d="M330,226 C520,186 720,168 900,176 V218 C720,202 520,212 330,226 Z" fill="var(--navy)"/>
    <path d="M0,238 C120,262 240,252 420,222 C560,198 700,200 770,212 C650,206 520,216 400,238 C240,266 110,270 0,254 Z" fill="var(--green)"/>
    <path d="M0,628 C180,596 380,648 560,660 C720,670 820,646 900,624 V1162 H0 Z" fill="url(#fadeBottom)"/>
    <path d="M0,596 C160,578 340,638 540,652 C340,668 150,646 0,664 Z" fill="var(--navy)"/>
    <path d="M420,654 C600,660 760,640 900,606 V632 C760,662 600,674 420,654 Z" fill="var(--green)"/>
    <defs>
      <linearGradient id="fadeBottom" x1="0" y1="0" x2="0" y2="1">
        <stop offset="0" stop-color="#ffffff"/>
        <stop offset="0.75" stop-color="#eeeff1"/>
        <stop offset="1" stop-color="#ffffff"/>
      </linearGradient>
    </defs>
  </svg>

  <div class="brand">
    <span class="brand-dot"></span>
    <span class="brand-name">Riverbend Trusted Home Care</span>
  </div>

  <header class="headline-block">
    <p class="kicker">Seeking care for your loved one?</p>
    <h1 class="headline">Lean On<br>Those Nearby</h1>
  </header>

  <section class="services">
    <h2>Our Services Include:</h2>
    <ul>
      <li>Experienced Certified Home Health<br>Aides/ Live In Home Health Aides/Companions</li>
      <li>Nursing Services</li>
      <li>Alzheimer’s and Dementia Care</li>
      <li>Respite Care</li>
      <li>Postoperative Care</li>
      <li>Post Rehabilitation Care</li>
      <li>Running Errands</li>
      <li>Light Housekeeping</li>
      <li>Assistance with Bathing, Feeding and Grooming</li>
      <li>Meal Preparation</li>
      <li>Laundry and Linen Washing</li>
      <li>Mail and Bill Organization</li>
      <li>Medication Management</li>
      <li>Accompanying to Doctor’s Appointments</li>
      <li>And much more!</li>
    </ul>
  </section>

  <p class="intro">As seasoned professionals, we know how to help our clients navigate and fulfill their various health care needs. Those nearby are here to help you get the attention that you merit.</p>

  <div class="cta">Call Riverbend Trusted Home Care<br>today to learn more about our<br>first-rate services!</div>
  <div class="cta-phone">
    <svg viewBox="0 0 24 24" aria-hidden="true"><circle cx="12" cy="12" r="11" fill="#ffffff"/><path d="M8.6 6.5l1.6 2.6-1 1.2c.7 1.6 2 2.9 3.6 3.6l1.2-1 2.6 1.6-.6 2c-4.6.2-9.3-4.5-9.1-9.1z" fill="var(--green)"/></svg>
    <span>1 555 0142</span>
  </div>

  <div class="gallery">
    <div class="gallery-photo one" role="img" aria-label="Photo of a nurse checking an elderly man's blood pressure"></div>
    <div class="gallery-photo two" role="img" aria-label="Photo of a caregiver comforting an elderly woman"></div>
    <div class="gallery-photo three" role="img" aria-label="Photo of a gloved hand cleaning a kitchen counter"></div>
  </div>

  <div class="footer-rule"></div>
  <footer class="footer">
    <span class="contact">
      <svg viewBox="0 0 18 18" aria-hidden="true"><circle cx="9" cy="9" r="9" fill="var(--green)"/><rect x="4.5" y="6" width="9" height="6.5" fill="none" stroke="#fff" stroke-width="1.2"/><path d="M4.5 6l4.5 3.6L13.5 6" fill="none" stroke="#fff" stroke-width="1.2"/></svg>
      hello@riverbendtrusted.com
    </span>
    <span class="contact">
      <svg viewBox="0 0 18 18" aria-hidden="true"><circle cx="9" cy="9" r="9" fill="var(--green)"/><path d="M6.3 4.5l1.3 2-.8 1c.5 1.2 1.5 2.2 2.7 2.7l1-.8 2 1.3-.5 1.5c-3.5.2-7-3.3-6.8-6.8z" fill="#fff"/></svg>
      1 555 0142
    </span>
    <span class="contact">
      <svg viewBox="0 0 18 18" aria-hidden="true"><circle cx="9" cy="9" r="9" fill="var(--green)"/><circle cx="9" cy="9" r="4.5" fill="none" stroke="#fff" stroke-width="1.1"/><ellipse cx="9" cy="9" rx="2" ry="4.5" fill="none" stroke="#fff" stroke-width="1.1"/><path d="M4.5 9h9" stroke="#fff" stroke-width="1.1"/></svg>
      www.riverbendtrusted.com
    </span>
  </footer>
</main>
</body>
</html>
```